Help us Create Excitement with a Food To Go Web Site Menu

We are seeking a design that can serve as a template for a Wordpress based website. The template will present the name (BrimBowl), present the menu items with price details, and contact details. The final design should NOT have the Mingle Kerb Eats subtitle anywhere in the site.
Our plan is to have the menu with basic graphic elements with the options to link to images/pictures of the menu item (perhaps linked via Snapgram or something like that if possible).
Updates

Target Market(s)

Home dining menu intended to offer perspective customers an understanding of what they will be enjoying.

Contact Information for Business Card

BrimBowl logo (without the Mingle Kerb Eats tag line included)
hi@brimbowl.com.au
Phone: XXXX XXX XXX (to be provided)

Coding

Coded - Design and coding required

Number of Pages Required

2 page

Requirements
Must have
• A bold and colourful presence that is also on the playful side.

A clearly readable menu layout that doesn't feel small based on the limited number of items that we offer at this time.
Nice to have
• A playful semi-graffiti based feel would be nice to convey a sense of playfulness.
Should not have
• The design should not have an overly Asian feel to it.

It appears many people are misreading the brief so I am adding this point to clarify one of the design requirements.
-- The final design should NOT have the Mingle Kerb Eats subtitle anywhere in the site, including the logo.

```html
<!DOCTYPE html>
<html lang="en">
<head>
<meta charset="utf-8">
<title>BrimBowl – Menu</title>
<link href="https://fonts.googleapis.com/css2?family=Poppins:ital,wght@0,300;0,400;0,500;0,600;0,700;1,600&family=Marcellus&display=swap" rel="stylesheet">
<style>
:root{
  --red:#f20000;
  --red-dark:#b30000;
  --maroon:#7a0e10;
  --ink:#1a1a1a;
  --grey:#555;
  --grey-light:#6d6d6d;
  --white:#ffffff;
  --footer:#262626;
  --footer-text:#e6e6e6;
  --food-a:#e8b873;
  --food-b:#b9692e;
  --food-c:#f4d79c;
}
*{box-sizing:border-box;margin:0;padding:0}
html,body{width:1200px;height:3622px;overflow:hidden}
body{position:relative;background:var(--white);font-family:"Poppins",sans-serif;color:var(--ink)}
.abs{position:absolute}

/* header */
.brand{left:118px;top:48px;font:700 52px/1 "Poppins",sans-serif;color:var(--ink);display:flex;align-items:center;gap:12px;z-index:5}
.brand-dot{width:22px;height:22px;border-radius:50%;background:var(--red)}
.nav{left:540px;top:34px;display:flex;align-items:center;z-index:5}
.nav a{font:500 18px/1 "Poppins",sans-serif;color:var(--ink);text-decoration:none;margin-right:38px}
.nav a.active{background:var(--red);color:var(--white);padding:10px 20px;border-radius:18px;margin-right:28px}
.cart{left:1040px;top:32px;z-index:5}
.cart-badge{left:1064px;top:28px;width:18px;height:18px;border-radius:50%;background:var(--red);color:#fff;font:600 11px/18px "Poppins",sans-serif;text-align:center;z-index:6}

/* photo bands */
.photo-band{left:0;width:1200px;background:radial-gradient(ellipse at 55% 45%,var(--food-c) 0%,var(--food-a) 40%,var(--food-b) 80%,#4a2a16 100%)}
.hero{top:90px;height:720px}
.touch{top:2240px;height:500px}
.edge{position:absolute;left:0;width:1200px}
.hero-text{left:0;width:1200px;text-align:center;color:var(--white);text-shadow:0 2px 8px rgba(0,0,0,.35)}
.hero-kicker{top:292px;font:600 36px/1 "Poppins",sans-serif}
.hero-main{top:350px;font:700 62px/1 "Poppins",sans-serif;display:flex;justify-content:center;align-items:flex-end;gap:12px}
.hero-main small{font:500 26px/1 "Poppins",sans-serif;margin-bottom:6px}
.hero-main .stack{font:500 22px/0.95 "Poppins",sans-serif;display:flex;flex-direction:column;margin-bottom:4px}
.menu-pill{left:525px;top:458px;width:150px;height:44px;border-radius:22px;background:var(--red);color:#fff;font:italic 600 20px/44px "Poppins",sans-serif;text-align:center}

/* section title */
.section-title{left:0;width:1200px;text-align:center}
.section-title .lead{top:835px;font:400 34px/1 "Poppins",sans-serif;color:var(--grey)}
.section-title .accent{top:880px;font:600 36px/1 "Poppins",sans-serif;color:var(--red)}

/* cards */
.card{width:395px;height:560px;background:var(--white);border:3px solid #e6e6e6;box-shadow:0 2px 6px rgba(0,0,0,.12);overflow:hidden}
.card.featured{background:var(--red);border-color:var(--red-dark)}
.card-media{position:absolute;left:4px;top:4px;width:381px;height:268px}
.card-body{position:absolute;left:32px;top:290px;width:330px}
.card-title{font:500 24px/1.2 "Poppins",sans-serif;color:var(--red-dark)}
.card-sub{font:300 19px/1.3 "Poppins",sans-serif;color:var(--grey);margin-top:4px}
.card-text{font:300 15px/25px "Poppins",sans-serif;color:var(--grey);margin-top:18px}
.featured .card-title,.featured .card-sub,.featured .card-text{color:var(--white)}
.card-foot{position:absolute;left:32px;top:484px;width:330px;height:42px;display:flex;align-items:center}
.price{font:600 22px/1 "Poppins",sans-serif;width:79px}
.price.text{font:600 17px/1.05 "Poppins",sans-serif}
.featured .price{color:var(--white)}
.order-btn{width:166px;height:40px;border-radius:20px;background:var(--red);color:#fff;font:500 15px/40px "Poppins",sans-serif;text-align:center;display:flex;align-items:center;justify-content:center;gap:8px}
.featured .order-btn{background:var(--white);color:var(--red)}
.gallery-btn{margin-left:auto;width:42px;height:42px;border-radius:50%;background:var(--maroon);display:flex;align-items:center;justify-content:center}
.featured .gallery-btn{background:var(--white)}

/* contact */
.touch-title{left:332px;top:2330px;font:400 46px/1 "Marcellus",serif;color:var(--white)}
.field{border:2px solid rgba(255,255,255,.85);background:rgba(40,20,10,.28);color:var(--white);font:400 15px/1 "Poppins",sans-serif;padding:14px 18px}
.send-btn{left:525px;top:2605px;width:140px;height:40px;border-radius:20px;background:var(--red);color:#fff;font:500 16px/40px "Poppins",sans-serif;text-align:center}

/* feed */
.feed-title{left:255px;top:2808px;font:700 30px/1 "Poppins",sans-serif}
.feed-text{left:255px;top:2852px;width:700px;font:400 15px/21px "Poppins",sans-serif;color:var(--ink)}
.tile{position:absolute}

/* footer */
.footer{left:0;top:3300px;width:1200px;height:322px;background:var(--footer);color:var(--footer-text)}
.f-head{font:500 15px/1 "Poppins",sans-serif;letter-spacing:.5px;color:var(--white)}
.f-links{font:400 16px/28px "Poppins",sans-serif}
.f-line{display:flex;align-items:flex-start;gap:12px;font:400 16px/20px "Poppins",sans-serif}
.news-input{left:778px;top:3483px;width:178px;height:36px;background:#eef1f4;border-radius:18px 0 0 18px;color:#555;font:400 13px/36px "Poppins",sans-serif;padding-left:22px}
.news-btn{left:955px;top:3483px;width:118px;height:36px;background:var(--maroon);border-radius:0 18px 18px 0;color:#fff;font:600 14px/36px "Poppins",sans-serif;text-align:center}
.f-rule{left:0;top:3555px;width:1200px;height:1px;background:#555}
.copy{left:118px;top:3582px;font:400 13px/1 "Poppins",sans-serif;color:var(--white)}
.social{left:960px;top:3584px;display:flex;gap:14px}
.social span{width:12px;height:12px;border-radius:50%;background:#999}
</style>
</head>
<body>

<!-- header -->
<div class="abs brand"><span class="brand-dot"></span>BrimBowl</div>
<nav class="abs nav">
  <a class="active" href="#">BrimBowl</a>
  <a href="#">The Menu</a>
  <a href="#">Price Details</a>
  <a href="#">Contact</a>
</nav>
<svg class="abs cart" width="36" height="34" viewBox="0 0 36 34" aria-hidden="true">
  <path d="M2 4h6l5 18h17l4-13H10" fill="none" stroke="#1a1a1a" stroke-width="2.4" stroke-linejoin="round"/>
  <path d="M13 13h19M14 17h17" stroke="#1a1a1a" stroke-width="1.6"/>
  <circle cx="15" cy="28" r="3" fill="#1a1a1a"/><circle cx="28" cy="28" r="3" fill="#1a1a1a"/>
</svg>
<div class="abs cart-badge">0</div>

<!-- hero -->
<div class="abs photo-band hero" role="img" aria-label="Close-up of a wooden spoon lifting creamy crab and corn soup">
  <svg class="edge" style="top:0" width="1200" height="40" viewBox="0 0 1200 40" preserveAspectRatio="none" aria-hidden="true">
    <path d="M0 0H1200V14L1172 9 1150 18 1120 10 1090 20 1060 8 1030 16 990 9 960 19 920 11 880 17 850 8 810 15 770 10 740 20 700 12 660 18 620 9 580 16 540 10 500 19 460 11 420 17 380 8 340 16 300 11 260 20 220 12 180 18 140 9 100 17 60 10 30 19 0 12Z" fill="#fff"/>
  </svg>
  <svg class="edge" style="bottom:0" width="1200" height="130" viewBox="0 0 1200 130" preserveAspectRatio="none" aria-hidden="true">
    <path d="M0 80L40 88 70 78 110 92 150 84 190 96 230 86 270 100 310 92 350 104 390 95 430 108 470 98 510 110 550 100 590 112 630 102 670 108 700 90 730 96 760 82 790 100 820 86 850 106 880 92 910 112 940 100 970 118 1000 104 1030 120 1060 108 1090 122 1120 110 1150 124 1180 114 1200 120V130H0Z" fill="#fff"/>
  </svg>
</div>
<div class="abs hero-text hero-kicker">DISCOVER WHAT`S NEW</div>
<div class="abs hero-text hero-main"><small>AND</small>ORDER<span class="stack"><span>WITH</span><span>PAYO</span></span>ONLINE</div>
<div class="abs menu-pill">Our Menu</div>
<svg class="abs" style="left:540px;top:505px" width="120" height="90" viewBox="0 0 120 90" aria-hidden="true">
  <g fill="none" stroke="#fff" stroke-width="2">
    <path d="M4 20L45 78M45 78l-2-14M45 78l-13-6"/>
    <path d="M62 4L64 82M64 82l-7-12M64 82l7-12"/>
    <path d="M98 18L80 80M80 80l-1-14M80 80l10-10"/>
  </g>
</svg>

<!-- section title -->
<div class="abs section-title lead" style="left:0;top:835px;width:1200px;text-align:center;font:400 34px/1 'Poppins',sans-serif;color:var(--grey)">What Makes</div>
<div class="abs section-title accent" style="left:0;top:880px;width:1200px;text-align:center;font:600 36px/1 'Poppins',sans-serif;color:var(--red)">Our Menus Special ?</div>

<!-- cards -->
<article class="abs card" style="left:178px;top:977px">
  <div class="card-media" role="img" aria-label="Bowl of beef noodle soup with fresh herbs" style="background:linear-gradient(135deg,#2c2a22,#6f8a3c 45%,#e9eee2 55%,#2a2620)"></div>
  <svg class="abs" style="left:4px;top:252px" width="381" height="24" viewBox="0 0 381 24" preserveAspectRatio="none" aria-hidden="true"><path d="M0 14L30 8 60 16 100 6 140 14 180 4 200 2 230 6 270 14 310 6 350 15 381 8V24H0Z" fill="#fff"/></svg>
  <div class="card-body">
    <h3 class="card-title">Beef Noodle Soup</h3>
    <p class="card-sub">Grandma</p>
    <p class="card-text">Just like Ba (Grandma) used to make. Our Pho takes 12 hours to make. We boil and reduce our own broth, using the freshest, locally sourced ingredients.</p>
  </div>
  <div class="card-foot">
    <span class="price">$14</span>
    <span class="order-btn"><svg width="14" height="16" viewBox="0 0 14 16" aria-hidden="true"><path d="M2 5h10l1 10H1z M4 5V3a3 3 0 016 0v2" fill="none" stroke="currentColor" stroke-width="1.6"/></svg>Add to Order</span>
    <span class="gallery-btn"><svg width="20" height="16" viewBox="0 0 20 16" aria-hidden="true"><rect x="1" y="1" width="18" height="14" rx="2" fill="none" stroke="#fff" stroke-width="1.6"/><path d="M3 13l5-6 4 4 2-2 3 4z" fill="#fff"/></svg></span>
  </div>
</article>

<article class="abs card featured" style="left:625px;top:975px">
  <div class="card-media" role="img" aria-label="Hands rolling fresh egg rolls on a woven tray" style="background:linear-gradient(135deg,#3a5a1c,#b98a7a 45%,#d9d5e6 75%,#2e4f1a)"></div>
  <svg class="abs" style="left:4px;top:252px" width="381" height="24" viewBox="0 0 381 24" preserveAspectRatio="none" aria-hidden="true"><path d="M0 12L40 6 80 16 120 5 160 12 200 4 240 14 280 6 320 15 360 7 381 12V24H0Z" fill="#f20000"/></svg>
  <div class="card-body">
    <h3 class="card-title">Egg Rolls</h3>
    <p class="card-sub">Life Changing</p>
    <p class="card-text">Our egg rolls are an experience not to be missed. They are provided either prepared and ready to eat or fresh and ready for pan frying at your convenience.</p>
  </div>
  <div class="card-foot">
    <span class="price">$10</span>
    <span class="order-btn"><svg width="14" height="16" viewBox="0 0 14 16" aria-hidden="true"><path d="M2 5h10l1 10H1z M4 5V3a3 3 0 016 0v2" fill="none" stroke="currentColor" stroke-width="1.6"/></svg>Add to Order</span>
    <span class="gallery-btn"><svg width="20" height="16" viewBox="0 0 20 16" aria-hidden="true"><rect x="1" y="1" width="18" height="14" rx="2" fill="none" stroke="#f20000" stroke-width="1.6"/><path d="M3 13l5-6 4 4 2-2 3 4z" fill="#f20000"/></svg></span>
  </div>
</article>

<article class="abs card" style="left:178px;top:1592px">
  <div class="card-media" role="img" aria-label="Spoonful of crab and corn soup" style="background:radial-gradient(ellipse at 50% 45%,#f4d79c,#e3aa5c 55%,#5a3518)"></div>
  <svg class="abs" style="left:4px;top:252px" width="381" height="24" viewBox="0 0 381 24" preserveAspectRatio="none" aria-hidden="true"><path d="M0 14L30 8 60 16 100 6 140 14 180 4 200 2 230 6 270 14 310 6 350 15 381 8V24H0Z" fill="#fff"/></svg>
  <div class="card-body">
    <h3 class="card-title">Crab Soup</h3>
    <p class="card-sub">Mmm So Good, So Fresh</p>
    <p class="card-text">We use fresh whole chunk crab meat served in a thick homemade chicken and pork bone-based broth that takes 8 hours to prepare.</p>
  </div>
  <div class="card-foot">
    <span class="price text">Market<br>Price</span>
    <span class="order-btn"><svg width="14" height="16" viewBox="0 0 14 16" aria-hidden="true"><path d="M2 5h10l1 10H1z M4 5V3a3 3 0 016 0v2" fill="none" stroke="currentColor" stroke-width="1.6"/></svg>Add to Order</span>
    <span class="gallery-btn"><svg width="20" height="16" viewBox="0 0 20 16" aria-hidden="true"><rect x="1" y="1" width="18" height="14" rx="2" fill="none" stroke="#fff" stroke-width="1.6"/><path d="M3 13l5-6 4 4 2-2 3 4z" fill="#fff"/></svg></span>
  </div>
</article>

<article class="abs card" style="left:625px;top:1592px">
  <div class="card-media" role="img" aria-label="Stacked tuna salad sandwiches on a banana leaf" style="background:linear-gradient(180deg,#2a2420,#e8d6a8 35%,#f3ead2 55%,#d8c28c 70%,#2f6a1f)"></div>
  <svg class="abs" style="left:4px;top:252px" width="381" height="24" viewBox="0 0 381 24" preserveAspectRatio="none" aria-hidden="true"><path d="M0 14L30 8 60 16 100 6 140 14 180 4 200 2 230 6 270 14 310 6 350 15 381 8V24H0Z" fill="#fff"/></svg>
  <div class="card-body">
    <h3 class="card-title">Tuna Salad Sandwich</h3>
    <p class="card-sub">Sweet, Sour &amp; Tangy</p>
    <p class="card-text">Just like Ba (Grandma) used to make. Our Pho takes 12 hours to make. We boil and reduce our own broth, using the freshest, locally sourced ingredients.</p>
  </div>
  <div class="card-foot">
    <span class="price">$14</span>
    <span class="order-btn"><svg width="14" height="16" viewBox="0 0 14 16" aria-hidden="true"><path d="M2 5h10l1 10H1z M4 5V3a3 3 0 016 0v2" fill="none" stroke="currentColor" stroke-width="1.6"/></svg>Add to Order</span>
    <span class="gallery-btn"><svg width="20" height="16" viewBox="0 0 20 16" aria-hidden="true"><rect x="1" y="1" width="18" height="14" rx="2" fill="none" stroke="#fff" stroke-width="1.6"/><path d="M3 13l5-6 4 4 2-2 3 4z" fill="#fff"/></svg></span>
  </div>
</article>

<!-- contact band -->
<div class="abs photo-band touch" role="img" aria-label="Blurred close-up of creamy crab soup on a wooden spoon">
  <svg class="edge" style="top:0" width="1200" height="40" viewBox="0 0 1200 40" preserveAspectRatio="none" aria-hidden="true">
    <path d="M0 0H1200V22L1170 14 1140 24 1100 12 1060 20 1020 10 980 22 940 14 900 24 860 12 820 20 780 8 740 18 700 10 660 22 620 12 580 20 540 8 500 18 460 10 420 22 380 12 340 20 300 10 260 22 220 14 180 24 140 12 100 20 60 10 20 22 0 14Z" fill="#fff"/>
  </svg>
  <svg class="edge" style="bottom:0" width="1200" height="40" viewBox="0 0 1200 40" preserveAspectRatio="none" aria-hidden="true">
    <path d="M0 16L30 24 70 14 110 26 150 18 190 28 230 16 270 26 310 14 350 28 390 18 430 30 470 20 510 28 550 16 590 26 630 18 670 30 710 20 750 28 790 14 830 26 870 18 910 28 950 16 990 26 1030 20 1070 30 1110 18 1150 26 1200 18V40H0Z" fill="#fff"/>
  </svg>
</div>
<h2 class="abs touch-title">Get In Touch</h2>
<div class="abs field" style="left:332px;top:2405px;width:258px;height:46px">Name</div>
<div class="abs field" style="left:610px;top:2405px;width:258px;height:46px">Email</div>
<div class="abs field" style="left:332px;top:2480px;width:536px;height:90px">Message</div>
<div class="abs send-btn">Send Now</div>

<!-- photo feed -->
<h2 class="abs feed-title">Snapgram</h2>
<p class="abs feed-text">Meet your fellow Humans! Show us your BRB style on Chirper, Snapgram or FaceBoard and tag @BRBW for a chance to win free tees and be featured on our site!</p>
<div class="tile" role="img" aria-label="Friends sharing a meal and drinks at a table" style="left:255px;top:2920px;width:318px;height:295px;background:linear-gradient(135deg,#d8b98c,#8a6a4a 50%,#3d3a44)"></div>
<div class="tile" style="left:397px;top:3047px;width:34px;height:34px;border-radius:50%;background:var(--red)" aria-hidden="true"></div>
<div class="tile" role="img" aria-label="Fresh egg rolls being prepared" style="left:585px;top:2920px;width:178px;height:142px;background:linear-gradient(135deg,#3a5a1c,#b98a7a 55%,#d9d5e6)"></div>
<div class="tile" role="img" aria-label="Crab soup on a wooden spoon" style="left:775px;top:2920px;width:170px;height:142px;background:radial-gradient(ellipse at 50% 45%,#f4d79c,#e3aa5c 60%,#5a3518)"></div>
<div class="tile" role="img" aria-label="Stacked tuna salad sandwiches" style="left:585px;top:3074px;width:178px;height:141px;background:linear-gradient(180deg,#2a2420,#e8d6a8 40%,#f3ead2 60%,#2f6a1f)"></div>
<div class="tile" role="img" aria-label="Bowl of beef noodle soup with herbs" style="left:775px;top:3074px;width:170px;height:141px;background:radial-gradient(circle at 45% 50%,#6f8a3c,#e9eee2 45%,#2c2a22 75%)"></div>

<!-- footer -->
<footer class="abs footer">
  <svg class="edge" style="top:-14px" width="1200" height="30" viewBox="0 0 1200 30" preserveAspectRatio="none" aria-hidden="true">
    <path d="M0 18L40 10 80 20 120 8 160 16 200 6 240 18 280 10 320 20 360 8 400 16 440 6 480 18 520 10 560 20 600 8 640 16 680 6 720 18 760 10 800 20 840 8 880 16 920 6 960 18 1000 10 1040 20 1080 8 1120 16 1160 6 1200 14V30H0Z" fill="#262626"/>
  </svg>
  <div class="abs f-head" style="left:120px;top:90px">CONTACT US</div>
  <div class="abs f-line" style="left:120px;top:126px">
    <svg width="14" height="18" viewBox="0 0 14 18" aria-hidden="true"><path d="M7 17s6-6.5 6-10.5A6 6 0 001 6.5C1 10.5 7 17 7 17z" fill="none" stroke="#ddd" stroke-width="1.4"/><circle cx="7" cy="6.5" r="2" fill="none" stroke="#ddd" stroke-width="1.4"/></svg>
    <span>Adress / Legal<br>Country Name, Streetl</span>
  </div>
  <div class="abs f-line" style="left:120px;top:178px">
    <svg width="14" height="16" viewBox="0 0 14 16" aria-hidden="true"><path d="M3 1l3 3-2 2c1 2 3 4 5 5l2-2 3 3-2 3C6 14 0 8 1 3z" fill="#ddd"/></svg>
    <span>+123 4567 8900</span>
  </div>
  <div class="abs f-line" style="left:120px;top:206px">
    <svg width="16" height="14" viewBox="0 0 16 14" aria-hidden="true"><rect x="1" y="2" width="14" height="10" fill="none" stroke="#ddd" stroke-width="1.3"/><path d="M1 2l7 6 7-6" fill="none" stroke="#ddd" stroke-width="1.3"/></svg>
    <span>hi@brimbowl.com.au</span>
  </div>

  <div class="abs f-head" style="left:405px;top:90px">QUICK LINKS</div>
  <div class="abs f-links" style="left:405px;top:118px">Home<br>BrimBowl<br>The Menu</div>

  <div class="abs f-head" style="left:581px;top:90px">QUICK LINKS</div>
  <div class="abs f-links" style="left:581px;top:118px">Price Details<br>Order Now<br>Contact Us</div>

  <div class="abs f-head" style="left:778px;top:90px">WRITE TO US</div>
  <div class="abs" style="left:778px;top:124px;width:320px;font:400 16px/24px 'Poppins',sans-serif">Provide your email below to subscribe to our newsletter</div>
</footer>
<div class="abs news-input">Email address</div>
<div class="abs news-btn">Subscribe</div>
<div class="abs f-rule"></div>
<div class="abs copy">Copyright 2020 BrimBowl</div>
<div class="abs social" aria-hidden="true"><span></span><span></span><span></span><span></span><span></span></div>

</body>
</html>
```